Kralto website design on shopify

Job Description:
As a web designer for Kralto, you will be the driving force behind designing and developing our new e-commerce website. Your responsibility will be to create an attractive, functional, and intuitive online shopping experience where customers can effortlessly discover and purchase high-quality supplements such as pre-workout, creatine, and protein shakes. Your design will play a crucial role in enhancing our brand and engaging our target audience.

Coding

Coded - Design and coding required

```html
<!DOCTYPE html>
<html lang="en">
<head>
<meta charset="utf-8">
<title>Kralto — High-Quality Supplements</title>
<link rel="stylesheet" href="https://fonts.googleapis.com/css2?family=Montserrat:wght@400;500;600;700;800&family=Libre+Baskerville:wght@700&display=swap">
<style>
:root{
  --purple:#8c4aa3;
  --purple-dark:#7a3d92;
  --ink:#1c1c1c;
  --text:#2b2b2b;
  --card:#efedea;
  --band:#f7f6f4;
  --footer:#1f1f1f;
  --white:#ffffff;
}
*{margin:0;padding:0;box-sizing:border-box}
html,body{width:1200px;height:4024px;overflow:hidden}
body{position:relative;background:var(--white);font-family:'Montserrat',sans-serif;color:var(--text)}
.abs{position:absolute}
/* header */
.site-header{left:0;top:0;width:1200px;height:82px;background:var(--white)}
.brand{left:130px;top:22px;display:flex;align-items:center;gap:10px}
.brand-mark{width:30px;height:30px;border-radius:50%;background:var(--purple)}
.brand-name{font-size:30px;font-weight:600;color:var(--purple);letter-spacing:1px}
.main-nav{left:414px;top:27px;display:flex;gap:31px;font-size:14px;font-weight:500;color:var(--ink)}
.main-nav a{color:inherit;text-decoration:none}
.main-nav .active{color:var(--purple);text-decoration:underline;text-underline-offset:4px}
.header-icons{left:1013px;top:26px;display:flex;gap:18px}
/* hero */
.hero{left:0;top:82px;width:1200px;height:579px;background:radial-gradient(ellipse at 60% 40%,#6b5a4e 0%,#2e2621 45%,#141110 100%)}
.hero-title{left:130px;top:393px;font-family:'Libre Baskerville',serif;font-weight:700;font-size:38px;line-height:48px;color:var(--white);letter-spacing:1px}
.btn{display:inline-flex;align-items:center;justify-content:center;background:var(--purple);color:var(--white);font-weight:800;text-decoration:none;border-radius:30px}
.hero-btn{left:130px;top:503px;width:148px;height:44px;font-size:16px;border:2px solid var(--white)}
.slider-count{left:574px;top:612px;display:flex;align-items:center;gap:10px;color:var(--white);font-size:13px}
/* headings */
.section-title{width:1200px;left:0;text-align:center;font-size:19px;font-weight:800;color:var(--ink);letter-spacing:.5px}
.title-rule{left:582px;width:36px;height:3px;background:var(--purple)}
/* product cards */
.product-card{width:223px;height:358px;background:var(--card);border-radius:3px}
.product-shot{left:48px;top:26px;width:127px;height:130px;border-radius:8px}
.product-name{left:0;top:216px;width:223px;text-align:center;font-size:13px;color:var(--text)}
.product-price{left:0;top:252px;width:223px;text-align:center;font-size:16px;color:var(--ink)}
.cart-btn{left:60px;top:295px;width:103px;height:30px;font-size:11px}
/* feature panels */
.feature-text{font-size:13px;line-height:17.5px}
.feature-title{font-size:20px;font-weight:800;letter-spacing:.3px}
.panel-purple{left:130px;top:1181px;width:427px;height:447px;background:var(--purple);color:var(--white)}
.panel-gray{left:642px;top:1669px;width:427px;height:447px;background:var(--card);color:var(--text)}
.photo{border-radius:2px}
/* category tiles */
.tile{width:304px;height:415px;border-radius:10px}
.tile-label{width:304px;text-align:center;font-size:16px;font-weight:700;color:var(--ink)}
.tile-btn{width:90px;height:26px;font-size:9px}
/* why choose */
.why-band{left:0;top:2714px;width:1200px;height:422px;background:var(--band)}
.why-icon{width:80px;height:80px;border-radius:50%;background:var(--purple);display:flex;align-items:center;justify-content:center}
.why-head{width:300px;text-align:center;font-size:16px;font-weight:600;line-height:26px;color:var(--ink)}
.why-text{width:270px;text-align:center;font-size:11.5px;line-height:16px;color:var(--text)}
/* footer */
.site-footer{left:0;top:3690px;width:1200px;height:334px;background:var(--footer);color:var(--white)}
.foot-head{font-size:14px;font-weight:800}
.foot-list{list-style:none;font-size:11.5px;line-height:18px}
.foot-text{font-size:11.5px;line-height:18px;width:270px}
.foot-rule{left:130px;top:242px;width:940px;height:1px;background:#3a3a3a}
.copyright{left:0;top:283px;width:1200px;text-align:center;font-size:11px}
</style>
</head>
<body>

<header class="abs site-header">
  <div class="abs brand"><span class="brand-mark"></span><span class="brand-name">Kralto</span></div>
  <nav class="abs main-nav">
    <a class="active" href="#">Home</a><a href="#">About Us</a><a href="#">Products</a><a href="#">Inspiration</a><a href="#">Blog</a><a href="#">Shop</a><a href="#">Contact Us</a>
  </nav>
  <div class="abs header-icons">
    <svg width="18" height="18" viewBox="0 0 18 18" fill="none" stroke="#1c1c1c" stroke-width="2"><circle cx="7.5" cy="7.5" r="5.5"/><line x1="11.5" y1="11.5" x2="16" y2="16"/></svg>
    <svg width="20" height="18" viewBox="0 0 20 18" fill="none" stroke="#1c1c1c" stroke-width="2"><path d="M1 2h3l2.5 10h10l2-7H5.5"/><circle cx="8" cy="16" r="1.3"/><circle cx="15" cy="16" r="1.3"/></svg>
  </div>
</header>

<section class="abs hero" role="img" aria-label="Athlete holding a shaker bottle in a dimly lit gym">
</section>
<h1 class="abs hero-title">HIGH-QUALITY<br>SUPPLEMENTS</h1>
<a class="abs btn hero-btn" href="#">SHOP NOW</a>
<div class="abs slider-count">
  <svg width="10" height="16" viewBox="0 0 10 16" fill="none" stroke="#fff" stroke-width="2"><path d="M8 1L2 8l6 7"/></svg>
  <span>1/3</span>
  <svg width="10" height="16" viewBox="0 0 10 16" fill="none" stroke="#fff" stroke-width="2"><path d="M2 1l6 7-6 7"/></svg>
</div>

<h2 class="abs section-title" style="top:697px">OUR PRODUCTS</h2>
<div class="abs title-rule" style="top:738px"></div>

<div class="abs product-card" style="left:130px;top:783px">
  <div class="abs product-shot" role="img" aria-label="Black whey protein tub" style="background:linear-gradient(#3a3a36,#1a1a18)"></div>
  <p class="abs product-name">Lorem Ipsum is sim</p><p class="abs product-price">$18.00</p>
  <a class="abs btn cart-btn" href="#">Add to cart</a>
</div>
<div class="abs product-card" style="left:369px;top:783px">
  <div class="abs product-shot" role="img" aria-label="Pill jar with orange capsules" style="background:linear-gradient(#e39a4a,#2a2a2a)"></div>
  <p class="abs product-name">Lorem Ipsum is sim</p><p class="abs product-price">$18.00</p>
  <a class="abs btn cart-btn" href="#">Add to cart</a>
</div>
<div class="abs product-card" style="left:607px;top:783px">
  <div class="abs product-shot" role="img" aria-label="White protein isolate tub" style="background:linear-gradient(#f4f4f4,#9ab8d4)"></div>
  <p class="abs product-name">Lorem Ipsum is sim</p><p class="abs product-price">$18.00</p>
  <a class="abs btn cart-btn" href="#">Add to cart</a>
</div>
<div class="abs product-card" style="left:846px;top:783px">
  <div class="abs product-shot" role="img" aria-label="Orange and grey whey protein tub" style="background:linear-gradient(#e08a3c,#8a8a8a)"></div>
  <p class="abs product-name">Lorem Ipsum is sim</p><p class="abs product-price">$18.00</p>
  <a class="abs btn cart-btn" href="#">Add to cart</a>
</div>

<section class="abs panel-purple">
  <h3 class="abs feature-title" style="left:76px;top:69px">SUPPLEMENTS</h3>
  <div class="abs" style="left:76px;top:112px;width:34px;height:3px;background:var(--white)"></div>
  <p class="abs feature-text" style="left:81px;top:145px;width:280px">Lorem ipsum dolor sit amet, consectetur adipiscing elit, sed do eiusmod tempor incididunt ut labore et dolore magna aliqua. Ut enim ad minim veniam, quis nostrud exercitation ullamco laboris nisi ut aliquip ex ea commodo consequat. Duis aute irure dolor in reprehenderit in voluptate velit esse.</p>
  <a class="abs btn" href="#" style="left:84px;top:321px;width:147px;height:44px;font-size:15px;border:2px solid var(--white);background:transparent">SHOP NOW</a>
</section>
<div class="abs photo" role="img" aria-label="Bearded man holding two supplement tubs" style="left:557px;top:1181px;width:512px;height:447px;background:linear-gradient(135deg,#f2f2f0,#d9d6d0 60%,#b8b0a6)"></div>

<div class="abs photo" role="img" aria-label="Woman in a kitchen with a shaker and supplement bottle" style="left:130px;top:1669px;width:512px;height:447px;background:linear-gradient(135deg,#e7e2dc,#cfc6bc 55%,#8fb4c8)"></div>
<section class="abs panel-gray">
  <h3 class="abs feature-title" style="left:65px;top:69px;color:var(--ink)">SUPPLEMENTS 1</h3>
  <div class="abs" style="left:68px;top:112px;width:34px;height:3px;background:var(--ink)"></div>
  <p class="abs feature-text" style="left:70px;top:145px;width:280px">Lorem ipsum dolor sit amet, consectetur adipiscing elit, sed do eiusmod tempor incididunt ut labore et dolore magna aliqua. Ut enim ad minim veniam, quis nostrud exercitation ullamco laboris nisi ut aliquip ex ea commodo consequat. Duis aute irure dolor in reprehenderit in voluptate velit esse.</p>
  <a class="abs btn" href="#" style="left:72px;top:320px;width:148px;height:44px;font-size:15px">SHOP NOW</a>
</section>

<div class="abs tile" role="img" aria-label="Black creatine tub with pink stripes" style="left:132px;top:2155px;background:linear-gradient(#f5f4f4,#ecebeb)"></div>
<div class="abs tile" role="img" aria-label="Protein shake in a shaker with powder scoop" style="left:448px;top:2155px;background:linear-gradient(#f2f1ef,#cdb8a2)"></div>
<div class="abs tile" role="img" aria-label="Black supplement bottle on yellow background" style="left:766px;top:2155px;background:linear-gradient(#f0d85a,#e3c440)"></div>
<p class="abs tile-label" style="left:132px;top:2590px">CREATINE</p>
<p class="abs tile-label" style="left:448px;top:2590px">PROTEIN SHAKES</p>
<p class="abs tile-label" style="left:766px;top:2590px">SUPPLEMENTS</p>
<a class="abs btn tile-btn" href="#" style="left:243px;top:2627px">SHOP NOW</a>
<a class="abs btn tile-btn" href="#" style="left:559px;top:2627px">SHOP NOW</a>
<a class="abs btn tile-btn" href="#" style="left:877px;top:2627px">SHOP NOW</a>

<section class="abs why-band">
  <h2 class="abs section-title" style="top:47px">WHY CHOOSE PEAK FORM</h2>
  <div class="abs title-rule" style="top:89px"></div>

  <div class="abs why-icon" style="left:212px;top:134px">
    <svg width="44" height="30" viewBox="0 0 44 30"><rect x="2" y="4" width="26" height="18" rx="2" fill="#fff"/><path d="M28 10h8l6 6v6H28z" fill="#fff"/><circle cx="10" cy="24" r="4" fill="#fff" stroke="#8c4aa3" stroke-width="2"/><circle cx="34" cy="24" r="4" fill="#fff" stroke="#8c4aa3" stroke-width="2"/><text x="15" y="17" font-family="Montserrat,sans-serif" font-size="8" font-weight="800" fill="#8c4aa3" text-anchor="middle">FREE</text></svg>
  </div>
  <div class="abs why-icon" style="left:559px;top:134px">
    <svg width="36" height="36" viewBox="0 0 36 36"><circle cx="18" cy="18" r="17" fill="#fff"/><path d="M18 7l3.2 6.6 7.2 1-5.2 5 1.3 7.2L18 23.4l-6.5 3.4 1.3-7.2-5.2-5 7.2-1z" fill="#8c4aa3"/></svg>
  </div>
  <div class="abs why-icon" style="left:898px;top:134px">
    <svg width="30" height="38" viewBox="0 0 30 38"><rect x="8" y="2" width="14" height="6" rx="1" fill="#fff"/><rect x="3" y="9" width="24" height="27" rx="3" fill="#fff"/><rect x="7" y="18" width="12" height="10" fill="#8c4aa3"/></svg>
  </div>

  <p class="abs why-head" style="left:102px;top:230px">Fast, free shipping<br>in the USA.</p>
  <p class="abs why-head" style="left:450px;top:230px">More than 1000<br>5-star reviews.</p>
  <p class="abs why-head" style="left:788px;top:230px">Quality products<br>at a fair price.</p>
  <p class="abs why-text" style="left:117px;top:288px">Lorem ipsum dolor sit amet, cons ectetur adipiscing elit, sed do eius mod tempor incididunt ut labore et dolore magna aliqua. Ut enim ad minim veniam, quis.</p>
  <p class="abs why-text" style="left:465px;top:288px">Lorem ipsum dolor sit amet, cons ectetur adipiscing elit, sed do eius mod tempor incididunt ut labore et dolore magna aliqua. Ut enim ad minim veniam, quis.</p>
  <p class="abs why-text" style="left:803px;top:288px">Lorem ipsum dolor sit amet, cons ectetur adipiscing elit, sed do eius mod tempor incididunt ut labore et dolore magna aliqua. Ut enim ad minim veniam, quis.</p>
</section>

<h2 class="abs section-title" style="top:3184px;left:-10px">BEST SELLERS</h2>
<div class="abs title-rule" style="top:3225px;left:572px"></div>

<div class="abs product-card" style="left:130px;top:3271px">
  <div class="abs product-shot" role="img" aria-label="Plain white supplement bottle" style="background:linear-gradient(#ffffff,#dedede)"></div>
  <p class="abs product-name">Lorem Ipsum is sim</p><p class="abs product-price">$18.00</p>
  <a class="abs btn cart-btn" href="#">Add to cart</a>
</div>
<div class="abs product-card" style="left:369px;top:3271px">
  <div class="abs product-shot" role="img" aria-label="Coral supplement bottle" style="background:linear-gradient(#f29a94,#f07a72)"></div>
  <p class="abs product-name">Lorem Ipsum is sim</p><p class="abs product-price">$18.00</p>
  <a class="abs btn cart-btn" href="#">Add to cart</a>
</div>
<div class="abs product-card" style="left:607px;top:3271px">
  <div class="abs product-shot" role="img" aria-label="Black supplement bottle with purple label" style="background:linear-gradient(#2a2a2a,#5a2a6e)"></div>
  <p class="abs product-name">Lorem Ipsum is sim</p><p class="abs product-price">$18.00</p>
  <a class="abs btn cart-btn" href="#">Add to cart</a>
</div>
<div class="abs product-card" style="left:846px;top:3271px">
  <div class="abs product-shot" role="img" aria-label="Collagen peptides tub with red label" style="background:linear-gradient(#1e1e1e,#d9334a 55%,#f2f2f2)"></div>
  <p class="abs product-name">Lorem Ipsum is sim</p><p class="abs product-price">$18.00</p>
  <a class="abs btn cart-btn" href="#">Add to cart</a>
</div>

<footer class="abs site-footer">
  <h4 class="abs foot-head" style="left:133px;top:54px">MENU</h4>
  <ul class="abs foot-list" style="left:135px;top:82px"><li>Home</li><li>About Us</li><li>Products</li><li>Inspiration</li><li>Blog</li><li>Shop</li><li>Contact Us</li></ul>
  <h4 class="abs foot-head" style="left:326px;top:54px">ABOUT</h4>
  <ul class="abs foot-list" style="left:328px;top:82px"><li>Our story</li><li>Shipping and returns</li><li>Contact</li><li>Blog</li></ul>
  <h4 class="abs foot-head" style="left:565px;top:54px">OUR MISSION</h4>
  <p class="abs foot-text" style="left:567px;top:82px">Lorem ipsum dolor sit amet, consectetur adipiscing elit, sed do eiusmod tempor incididunt ut labore et dolore magna aliqua. Ut enim ad minim veniam, quis nostrud exer citation ullamco laboris nisi ut aliquip ex ea commodo consequat.</p>
  <div class="abs brand" style="left:880px;top:94px"><span class="brand-mark"></span><span class="brand-name">Kralto</span></div>
  <div class="abs foot-rule"></div>
  <p class="abs copyright">Copyright © 2023 All Rights Reserved</p>
</footer>

</body>
</html>
```